Saint Brigid of Meadowvale banners

In need of two banners designed.
Product Details:
Imprint Area:
Banner stands: 2-33.5"W x 79"H (full color),

Product Size:
Two Banner Stands: 34"W x 83"H including base,
See attached for specifics

* We would like the logo and "Annual Fundraiser" added above the logo or on either side of the logo.
* The problem we were running in to was that "Annual" and "Fundraiser" are not equal in length.

Banner Stand
* This will talk about what the foundation is
Logo with "Annual Fundraiser" incorporated
*You can also visit our website www.sbmparishdunwick.org and go to the Learning Trust page for more info
Q: Who benefits from the foundation?
A: All Saint Brigid of Meadowvale(SBM) parishioners and local people looking to enhance their faith.
Q: What does the foundation fund?
A: All learning opportunities provided by the parish
*KERYX and Adult Bible Studies
*Faith Formation (Nursery-12 th Grade)
*RCIA and Sacramental Prep
*Books and CD's distributed during Lent and Advent
*SBM Elementary and Middle School and Vacation Bible School
*Parish Library and Mission

Banner(Horizontal)
* This is going to talk about our needs. I'm thinking on the top we could write something like:
Q: How can I help?
A: Donate your time, talent, and treasure

* Then we have 2 ways they can help: Volunteer and Donate
VOLUNTEER
Time: Can you help plan before, during, or after the event?
Talent: Do you have a special talent that might help us plan?
creative: help with decor or ideas
tech savy: help with social media and website, putting together slideshow
marketing: help get the word out
sales and outgoing personality: help solicit donations
DONATE
Talent: Do you have a special talent that you may be able to use to make an auction item? Could you knit a blanket, create a piece of art, offer a service like personal training or a hair cut? Are you the hostess with the mostest and would like to donate a party for someone?
Treasure: Do you own a business that could donate services or goods? Do you have a vacation home you would be willing to rent out? Would you be willing to donate money towards the planning or to the foundation?

*If there is room across the bottom we could put "Food * Drinks * Band * Silent/Live Auction"

Target Market(s)

Parishioners of Church

Industry/Entity Type

Non Profit

Font styles to use
Serif
Sans Serif

Colors
3276b5
0455a3

Requirements
Must have
• * Generic enough to be used year after year
• * Easy to read and not to overwhelming
Nice to have
• I would love to see some graphics included. You can add to my choosen colors if you think colorful is better

```html
<!DOCTYPE html>
<html lang="en">
<head>
<meta charset="utf-8">
<title>Learning Trust – Annual Fundraiser Banner</title>
<link rel="stylesheet" href="https://fonts.googleapis.com/css2?family=Montserrat:wght@600;700;800;900&family=Bowlby+One&display=swap">
<style>
  :root{
    --navy:#14295e;
    --navy-light:#2a4d9a;
    --lime:#9cc33b;
    --lime-dark:#7ea22a;
    --green-text:#2f5a1c;
    --yellow:#f7c52b;
    --yellow-dark:#e0a91a;
    --grey-top:#f2f3f5;
    --grey-bottom:#cfd3d8;
    --ink:#1b1b1f;
    --time:#8cbb3a;
    --talent:#1aa3dc;
    --talent-donate:#b54a9c;
    --treasure:#f2a31e;
  }
  *{margin:0;padding:0;box-sizing:border-box;}
  html,body{width:1200px;height:2972px;overflow:hidden;}
  body{
    position:relative;
    font-family:"Montserrat",Arial,sans-serif;
    background:linear-gradient(180deg,var(--grey-top) 30%,var(--grey-bottom) 100%);
    color:var(--ink);
  }
  .header-shape{position:absolute;left:0;top:0;width:1200px;height:900px;}
  .title-band{
    position:absolute;left:0;top:148px;width:1200px;height:410px;
    background:var(--lime);
  }
  .brand{
    position:absolute;left:80px;top:200px;width:400px;
    color:#fff;font-weight:800;text-align:center;
  }
  .brand-mark{display:block;width:70px;height:70px;background:#fff;margin:0 auto 24px;}
  .brand-name{font-size:52px;line-height:1.05;letter-spacing:2px;}
  .event-title{
    position:absolute;left:515px;top:262px;
    color:#fff;font-weight:800;font-size:96px;line-height:0.98;letter-spacing:0;
    white-space:nowrap;
  }
  .question{position:absolute;left:0;top:640px;width:1010px;height:126px;}
  .question span,.answer span{position:absolute;font-weight:800;}
  .question span{left:140px;top:32px;font-size:48px;color:var(--navy);white-space:nowrap;}
  .answer{position:absolute;left:290px;top:790px;width:910px;height:200px;}
  .answer span{left:95px;top:40px;font-size:42px;line-height:1.22;color:var(--green-text);text-align:center;width:780px;}
  .section-heading{
    position:absolute;left:37px;
    font-family:"Bowlby One",Impact,sans-serif;font-size:76px;line-height:1;color:var(--ink);
    letter-spacing:1px;
  }
  .heading-volunteer{top:1068px;}
  .heading-donate{top:1846px;}
  .item{position:absolute;left:37px;width:1130px;}
  .item-icon{
    position:absolute;left:0;top:0;width:58px;
    display:flex;justify-content:center;padding-top:14px;
  }
  .item-icon svg{width:46px;height:46px;}
  .item-body{margin-left:200px;width:930px;}
  .item-title{font-weight:900;font-size:54px;line-height:1;margin-bottom:12px;margin-left:12px;}
  .item-list{list-style:none;}
  .item-list li{font-weight:700;font-size:35px;line-height:1.22;margin-bottom:16px;padding-left:22px;text-indent:-22px;}
  .item-list li::before{content:"• ";}
  .item-time{top:1156px;} .item-time .item-icon{height:120px;background:var(--time);} .item-time .item-title{color:var(--time);}
  .item-talent{top:1440px;} .item-talent .item-icon{height:120px;background:var(--talent);} .item-talent .item-title{color:var(--talent);}
  .item-talent-donate{top:1924px;} .item-talent-donate .item-icon{height:335px;background:var(--talent-donate);} .item-talent-donate .item-title{color:var(--talent-donate);}
  .item-treasure{top:2322px;} .item-treasure .item-icon{height:340px;background:var(--treasure);} .item-treasure .item-title{color:var(--treasure);}
</style>
</head>
<body>
  <svg class="header-shape" viewBox="0 0 1200 900" aria-hidden="true">
    <defs>
      <linearGradient id="navyFade" x1="0" y1="0" x2="0" y2="1">
        <stop offset="0" stop-color="#2a4d9a"/>
        <stop offset="0.25" stop-color="#14295e"/>
        <stop offset="1" stop-color="#14295e"/>
      </linearGradient>
    </defs>
    <path d="M0 0 H1200 V820 C850 700 350 720 0 790 Z" fill="url(#navyFade)"/>
  </svg>

  <div class="title-band"></div>

  <div class="brand">
    <span class="brand-mark"></span>
    <div class="brand-name">LEARNING<br>TRUST</div>
  </div>

  <h1 class="event-title">ANNUAL<br>FUNDRAISER</h1>

  <div class="question">
    <svg width="1010" height="126" viewBox="0 0 1010 126" aria-hidden="true">
      <polygon points="1010,0 1010,126 945,126" fill="var(--yellow-dark)"/>
      <polygon points="0,8 990,0 950,118 0,126" fill="var(--yellow)"/>
    </svg>
    <span>Q: How can I help?</span>
  </div>

  <div class="answer">
    <svg width="910" height="200" viewBox="0 0 910 200" aria-hidden="true">
      <polygon points="50,0 260,0 240,40 40,40" fill="var(--lime-dark)"/>
      <polygon points="45,22 910,22 910,200 60,200" fill="var(--lime)"/>
    </svg>
    <span>A: Sacrificial giving! Share your<br>TIME, TALENT, and TREASURE</span>
  </div>

  <h2 class="section-heading heading-volunteer">VOLUNTEER</h2>

  <section class="item item-time">
    <div class="item-icon">
      <svg viewBox="0 0 56 56" aria-hidden="true"><circle cx="28" cy="28" r="23" fill="none" stroke="#fff" stroke-width="5"/><path d="M28 14 V29 L38 36" fill="none" stroke="#fff" stroke-width="5" stroke-linecap="round"/></svg>
    </div>
    <div class="item-body">
      <h3 class="item-title">TIME:</h3>
      <ul class="item-list">
        <li>Are you available to help plan the event?</li>
        <li>Could you help with set up the day of the event?</li>
        <li>Want to help us wrap up after the event?</li>
      </ul>
    </div>
  </section>

  <section class="item item-talent">
    <div class="item-icon">
      <svg viewBox="0 0 56 56" aria-hidden="true"><polygon points="28,4 34,21 52,21 38,32 43,50 28,39 13,50 18,32 4,21 22,21" fill="#fff"/></svg>
    </div>
    <div class="item-body">
      <h3 class="item-title">TALENT:</h3>
      <ul class="item-list">
        <li>Are you creative? Help with decor or ideas.</li>
        <li>Tech savy? Help with website and multi media.</li>
        <li>Love to spread the word? Help gossip about our event on social media</li>
        <li>Outgoing? Help solicit donations.</li>
      </ul>
    </div>
  </section>

  <h2 class="section-heading heading-donate">DONATE</h2>

  <section class="item item-talent-donate">
    <div class="item-icon">
      <svg viewBox="0 0 56 56" aria-hidden="true"><polygon points="28,4 34,21 52,21 38,32 43,50 28,39 13,50 18,32 4,21 22,21" fill="#fff"/></svg>
    </div>
    <div class="item-body">
      <h3 class="item-title">TALENT:</h3>
      <ul class="item-list">
        <li>Do you have a special talent that you may be able to use to make an auction item?</li>
        <li>Could you knit a blanket, create a piece of art, offer a service like personal training or a hair cut?</li>
        <li>Are you the hostess with the mostest and would like to donate a party for someone?</li>
      </ul>
    </div>
  </section>

  <section class="item item-treasure">
    <div class="item-icon">
      <svg viewBox="0 0 56 56" aria-hidden="true"><rect x="6" y="8" width="44" height="40" fill="none" stroke="#fff" stroke-width="5"/><rect x="20" y="20" width="16" height="16" fill="none" stroke="#fff" stroke-width="4"/></svg>
    </div>
    <div class="item-body">
      <h3 class="item-title">TREASURE:</h3>
      <ul class="item-list">
        <li>Do you own a business that could donate services or goods?</li>
        <li>Do you have a vacation home you would be willing to rent out?</li>
        <li>Would you be willing to donate money towards the planning or to the foundation?</li>
      </ul>
    </div>
  </section>
</body>
</html>
```